ATM Website-Great Opportunity for Portability

Hey We need YOU to help us make our ATM (Automatic Teller Machine)Website!!) We are a million dollar business that will look great on your portfolio! Our Name is "CORNER CASH POINT"
Previous ATM business (now sold) was www.cashkiosqo.com.au (site being pulled down so look at it fast!)
The winner will get the same package that we will giving to the winner of our other project! (worth over $9,000)
http://jobs.briefhive.com/job.aspx?id=4827
**we are making a series of sites/applications Winners will be solo invited to work on all upcoming projects of that catigory**
***we are also looking for Outstanding freelance guys to work with on all future projects***
Main Points!!
1: one main page (that is not a blog!)
2: Then the Theme!
3: I don't want it to look like a word-press
I.e like this guys Word press http://www.trevsiteworks.com/
See how he has one main page then the rest are WP Theme :)
Key points to the Home Page!
See attached pic for the menu's needed and the call now key.
Main page needs to have
1. Clean, uncluttered, and follow the feel of our LOGO (attached) Be creative but simplistic with the page. Round curves are good)
2. Large hero images of happy poeple in the community but not looking too stocky or contrived - natural smiles, natural expressions, With Image of OUR ATM on the page!
3. Easy navigation
4: (3 big buttons like on our competitors site
(http://www.patronmoneybox.com.au/) With the titles
(get an ATM (and beside it "for your business")
(Own an ATM (increase your investment Portfolio)
(Latest ATM (See an ATM in action)
For the Theme Page,
It must flow on from the main menu but have a bread crum trail on the page of all the sub links somewhere on the left of the page (or somewhere else that might look better.
Theme page should have a Call now or email now option!! If you can fit in 2 without it looking cluttered that would be good.
I will attach our brochures so you can get a feel of our product.
Also you should be able to extract images from our brochure using QUILLOR PDF EDITOR or similar PDF editor if needed!!
logo attached and also found at www.cornercashpoint.com.au
Good Fonts to use!
Helvetica Neue LT (bold thin ect)
Helvetica Neue LT Com
Target Market(s)
Business Owners and Investors
Industry/Entity Type
Investment
Requirements
Must have
- The Call now Features in the attached file, Clean layout
Should not have
- Should not look like stock photo's and a cheap website or a template...

```html
<!DOCTYPE html>
<html lang="en">
<head>
<meta charset="utf-8">
<title>Corner Cash Point – Home</title>
<link rel="stylesheet" href="https://fonts.googleapis.com/css2?family=Mulish:wght@400;700;800&family=Noto+Sans:wght@400;700&display=swap">
<style>
:root{
  --bg:#ebebeb;
  --green:#7cbf2c;
  --green-dark:#5e9e1a;
  --green-light:#a9dc58;
  --band-top:#d6f79a;
  --band-bottom:#a6da56;
  --ink:#1b1b1b;
  --grey:#8a8a8a;
  --dark:#2a2a2a;
  --white:#ffffff;
  --photo-street:#8a8b85;
  --photo-face:#d9c2a8;
}
*{margin:0;padding:0;box-sizing:border-box}
html,body{width:1200px;height:843px;overflow:hidden}
body{position:relative;background:linear-gradient(180deg,#f0f0f0 0%,var(--bg) 60%,#e6e6e6 100%);font-family:"Noto Sans",Verdana,sans-serif;color:var(--ink)}
.abs{position:absolute}

/* header */
.brand{left:195px;top:11px;display:flex;align-items:center;gap:8px}
.brand-mark{width:100px;height:100px;border-radius:50%;background:var(--green)}
.brand-name{font-family:"Mulish",sans-serif;font-weight:400;font-size:20px;color:var(--grey);letter-spacing:-.3px}
.search{left:818px;top:36px;width:184px;height:19px;border:1px solid #b9b9b9;border-radius:10px;background:var(--white);overflow:hidden}
.search-hint{position:absolute;left:9px;top:2px;font-size:9px;color:#aaa;letter-spacing:.5px}
.search-go{position:absolute;right:0;top:0;width:27px;height:100%;background:var(--green)}
.promo{right:198px;top:68px;font-family:"Mulish",sans-serif;font-size:13px;text-align:right}
.promo b{font-weight:800;font-size:15px}
.callnow{right:198px;top:84px;font-family:"Mulish",sans-serif;font-size:21px;white-space:nowrap}
.callnow b{font-weight:800;font-size:26px}

/* nav */
.nav{left:195px;top:122px;width:808px;height:31px;border-radius:14px;background:linear-gradient(180deg,var(--green-light),var(--green));display:flex;align-items:center;font-family:"Mulish",sans-serif;font-size:12.5px;color:var(--white);overflow:hidden}
.nav .home{width:69px;height:100%;background:var(--dark);display:flex;align-items:center;justify-content:center;font-weight:800;font-size:14px;border-radius:14px 0 0 14px}
.nav a{color:var(--white);text-decoration:none;padding:0 8px}
.nav i{font-style:normal;opacity:.9}
.dropdown{left:265px;top:153px;width:175px;background:linear-gradient(180deg,#fff,#efefef);list-style:none;font-size:9.5px;z-index:3}
.dropdown li{height:20px;line-height:20px;padding-left:22px;border-bottom:1px dotted #aaa;position:relative}
.dropdown li::before{content:"›";position:absolute;left:10px;font-weight:700}

/* hero */
.hero{left:195px;top:160px;width:808px;height:296px;border-radius:12px;background:#dcdcdc}
.hero-photo{left:200px;top:164px;width:540px;height:288px;border-radius:10px 0 0 10px;background:linear-gradient(100deg,var(--photo-street) 0%,#b8b8b0 45%,#c6d7a8 60%,#8c8f86 100%)}
.dots{left:216px;top:432px;display:flex;gap:3px}
.dots span{width:14px;height:14px;border-radius:50%;border:2px solid var(--white)}
.dots span:first-child{background:#333}
.story{left:740px;top:164px;width:259px;height:288px;background:var(--white);border-radius:0 10px 10px 0;padding:12px 12px 12px 14px}
.story h2{font-family:"Mulish",sans-serif;font-weight:800;font-size:14px;letter-spacing:-.3px;color:var(--green);margin-left:-2px;white-space:nowrap}
.story p{font-size:10px;line-height:12px;margin-top:5px;color:#111}
.questions{left:673px;top:371px;width:326px;height:81px;background:linear-gradient(180deg,var(--green-light),var(--green));border-radius:12px 0 10px 0}
.questions h3{position:absolute;left:3px;top:7px;font-family:"Mulish",sans-serif;font-weight:800;font-size:15px}
.field{position:absolute;left:4px;width:146px;height:21px;background:var(--white);border:1px solid #555;font-size:10.5px;padding:3px 4px;color:#444}
.contact{left:828px;top:404px;width:41px;height:41px;border-radius:50%;background:#2f2f2f;color:var(--white);font-family:"Mulish",sans-serif;font-weight:700;font-size:9.5px;line-height:11px;text-align:center;padding-top:9px}
.agent{left:863px;top:303px;width:135px;height:135px;border-radius:50%;background:var(--green);display:flex;align-items:center;justify-content:center}
.agent div{width:113px;height:113px;border-radius:50%;background:var(--white);display:flex;align-items:center;justify-content:center}
.agent div span{width:93px;height:93px;border-radius:50%;background:radial-gradient(circle at 50% 45%,var(--photo-face),#7fbc3a 75%)}

/* feature cards */
.card{top:490px;width:256px;height:146px}
.card svg{position:absolute;left:0;top:0}
.card .pic{position:absolute;left:24px;top:28px;width:96px;height:96px;border-radius:50%}
.card h3{position:absolute;right:6px;top:8px;font-family:"Mulish",sans-serif;font-weight:800;font-size:19px;text-align:right;color:#111;line-height:22px;white-space:nowrap}
.card h4{position:absolute;right:6px;font-family:"Mulish",sans-serif;font-weight:700;font-size:12.5px;line-height:16px;color:var(--white);text-align:right;white-space:nowrap}
.card h4.tight{font-size:11.5px;letter-spacing:-.5px}
.card p{position:absolute;left:141px;width:112px;font-size:9.5px;line-height:11px;color:#111}
.card a{position:absolute;left:141px;font-size:10px;font-weight:700;color:#111;text-decoration:underline}

/* footer band */
.band{left:0;top:682px;width:1200px;height:130px;background:linear-gradient(180deg,var(--band-top),var(--band-bottom))}
.contact-line{font-family:"Mulish",sans-serif;font-weight:700;white-space:nowrap}
.divider{left:199px;top:746px;width:382px;border-top:1px dotted #8aa86a}
.testi h3{font-family:"Mulish",sans-serif;font-weight:800;font-size:15px;color:var(--green-dark)}
.quote{left:643px;top:716px;width:366px;font-size:10.5px;line-height:13px}
.more{right:198px;top:752px;font-size:9.5px;font-weight:700}
.author{left:643px;top:777px;font-size:10px;font-weight:700;line-height:12px;letter-spacing:.3px}
.bottom{left:0;top:812px;width:1200px;height:31px;background:var(--dark);color:var(--white);font-size:9.5px;font-weight:700;letter-spacing:.4px}
.bottom .copy{position:absolute;left:196px;top:9px}
.bottom .find{position:absolute;left:812px;top:9px}
.social{position:absolute;top:5px;width:22px;height:22px;border-radius:3px}
</style>
</head>
<body>

<header>
  <div class="abs brand">
    <span class="brand-mark"></span>
    <span class="brand-name">CORNER CASH POINT</span>
  </div>
  <div class="abs search"><span class="search-hint">Search ...</span><span class="search-go"></span></div>
  <div class="abs promo">Want a <b>FREE ATM</b> for your business?</div>
  <div class="abs callnow">Call Now: <b>1300 482 207</b></div>
</header>

<nav class="abs nav">
  <span class="home">Home</span>
  <a>About CCP</a><i>|</i><a>Investors</a><i>|</i><a>Product &amp; Services</a><i>|</i><a>Get a free ATM</a><i>|</i><a>Giving back</a><i>|</i><a>Who has one</a><i>|</i><a>Media</a><i>|</i><a>Careers</a>
</nav>
<ul class="abs dropdown">
  <li>Naviation Link 1</li><li>Naviation Link 2</li><li>Naviation Link 3</li><li>Naviation Link 4</li>
</ul>

<section>
  <div class="abs hero"></div>
  <div class="abs hero-photo" role="img" aria-label="Photo of a couple using a street ATM while holding a map"></div>
  <div class="abs dots"><span></span><span></span><span></span><span></span><span></span></div>
  <div class="abs story">
    <h2>Giving back to your community</h2>
    <p>We believe in the local community! with every transaction we donate 10% to a 40% of all profits to charity like the Young Hands Foundation and or the local community such as your local NeighbourMart store.</p>
  </div>
  <div class="abs questions">
    <h3>Questions?</h3>
    <div class="field" style="top:31px">enter number...</div>
    <div class="field" style="top:55px">enter email..</div>
  </div>
  <div class="abs contact">Contact<br>Me</div>
  <div class="abs agent"><div><span role="img" aria-label="Photo of a smiling support agent wearing a headset"></span></div></div>
</section>

<section>
  <div class="abs card" style="left:195px">
    <svg width="256" height="146" viewBox="0 0 256 146"><path d="M72 0H256V146H72A73 73 0 0 1 72 0Z" fill="var(--green)"/><circle cx="72" cy="76" r="66" fill="var(--white)"/><circle cx="72" cy="76" r="70" fill="none" stroke="var(--green-light)" stroke-width="4"/></svg>
    <span class="pic" role="img" aria-label="Photo of a woman using an ATM keypad" style="background:linear-gradient(135deg,#6f7478,#c9ccc9)"></span>
    <h3>Get An ATM</h3><h4 style="top:29px">For Your Business</h4>
    <p style="top:59px">Free ATM that brings the customers in!</p><a style="top:84px">Read More</a>
  </div>
  <div class="abs card" style="left:471px">
    <svg width="256" height="146" viewBox="0 0 256 146"><path d="M72 0H256V146H72A73 73 0 0 1 72 0Z" fill="var(--green)"/><circle cx="72" cy="76" r="66" fill="var(--white)"/><circle cx="72" cy="76" r="70" fill="none" stroke="var(--green-light)" stroke-width="4"/></svg>
    <span class="pic" role="img" aria-label="Illustration of rising green bar chart with an arrow" style="background:linear-gradient(135deg,#ffffff,#8fd24a)"></span>
    <h3>Own An ATM</h3><h4 class="tight" style="top:29px">Increase you<br>Investment Portfolio</h4>
    <p style="top:67px">Earn a real passive income with great returns!</p><a style="top:102px">Read More</a>
  </div>
  <div class="abs card" style="left:749px">
    <svg width="256" height="146" viewBox="0 0 256 146"><path d="M72 0H256V146H72A73 73 0 0 1 72 0Z" fill="var(--green)"/><circle cx="72" cy="76" r="66" fill="var(--white)"/><circle cx="72" cy="76" r="70" fill="none" stroke="var(--green-light)" stroke-width="4"/></svg>
    <span class="pic" role="img" aria-label="Photo of a shop owner standing beside a newly installed ATM" style="background:linear-gradient(135deg,#5d6b80,#e6e1d8)"></span>
    <h3>Latest ATM’s</h3><h4 style="top:29px">See an ATM<br>in Action</h4>
    <p style="top:67px">Find out who has just got one!</p><a style="top:102px">Read More</a>
  </div>
</section>

<footer>
  <div class="abs band"></div>
  <svg class="abs" style="left:195px;top:686px" width="56" height="54" viewBox="0 0 56 54"><rect x="2" y="4" width="50" height="46" rx="9" fill="var(--green)" transform="rotate(-8 27 27)"/><path d="M17 14c-3 3-3 8 1 15s10 12 15 13c3 1 6-1 8-4l-6-5-4 3c-4-2-8-7-9-11l3-3-4-8z" fill="var(--white)"/></svg>
  <div class="abs contact-line" style="left:267px;top:697px;font-size:16px">Call Now: <span style="font-size:31px;font-weight:800;vertical-align:-2px">1300 482 207</span></div>
  <div class="abs divider"></div>
  <svg class="abs" style="left:196px;top:751px" width="60" height="54" viewBox="0 0 60 54"><g transform="rotate(-14 30 27)"><rect x="6" y="10" width="48" height="34" fill="var(--white)" stroke="#9a9a9a"/><path d="M8 12h44L30 30z" fill="var(--green)"/><path d="M8 42l16-14M52 42L36 28" stroke="var(--green-dark)" stroke-width="2"/></g></svg>
  <div class="abs contact-line" style="left:266px;top:763px;font-size:16px">Email : <span style="font-size:27px;font-weight:700">team@ccpoint.com.au</span></div>

  <div class="abs testi" style="left:641px;top:692px"><h3>Testimonials</h3></div>
  <p class="abs quote">"We are surprised to see how much extra business just walks in the door because ATM' -</p>
  <div class="abs more">Read More</div>
  <div class="abs author">Leafwise, Leafwise Health Food<br>Leafwise Real Food,</div>

  <div class="abs bottom">
    <span class="copy">Copyright © 2010 cornercashpoint.com.au | All Rights Reserved</span>
    <span class="find">Find us on:</span>
    <span class="social" style="left:877px;background:#3b5a9a"></span>
    <span class="social" style="left:903px;background:#2fa8de"></span>
    <span class="social" style="left:929px;background:#1d77b5"></span>
    <span class="social" style="left:955px;background:#c4302b"></span>
    <span class="social" style="left:981px;background:#17a9e1"></span>
  </div>
</footer>

</body>
</html>
```